Pelwick Renovations Letterhead

Pelwick does not do actual renovation, but rather handles high end project management of renovation (primarily residential with an eye toward commercial and International) The renovation work could look very different between projects. This company works directly with the clients and manages the work of contractors, architects and interior designers (either subcontracted directly by Pelwick or hired by the client and entrusted to Pelwick to manage). Clients are high end in the economic scale and all materials should speak to that audience. Provoke a sense of change, openness and imagination, trust and integrity. The owner is female, but the audience will be heavily slanted male. It should not be a "feminine" or "masculine" looking . If anything, slant more on the masculine side.

Clean, simple, yet creative and artistically appealing. The logo should be clear and not competing with too many surrounding design elements.

There is a contest also on for business card. Please check that section if you would like to compete for both.

Get your creative juices going!

Target Market(s)

High end cients. Additional audience: professionals (architects, etc...) designers, contractors

Industry/Entity Type

Residential

Requirements
Must have
• Logo must be included in all materials

```html
<!DOCTYPE html>
<html lang="en">
<head>
<meta charset="utf-8">
<title>Pelwick Renovations Stationery</title>
<link rel="stylesheet" href="https://fonts.googleapis.com/css2?family=Jost:wght@500&family=Arimo:wght@400&display=swap">
<style>
:root{
  --teal:#1aa89c;
  --ink:#3d3d3d;
  --paper:#ffffff;
  --backdrop:#ecebe8;
  --edge:#9a9a9a;
}
*{margin:0;padding:0;box-sizing:border-box}
html,body{width:1200px;height:1177px;overflow:hidden}
body{background:var(--backdrop);position:relative;font-family:"Arimo",Arial,sans-serif;color:var(--ink)}
.letterhead{position:absolute;left:58px;top:37px;width:841px;height:1086px;background:var(--paper);border:1px solid var(--edge)}
.business-card{position:absolute;left:641px;top:426px;width:521px;height:296px;background:var(--paper);border:1px solid var(--edge)}
.header-band{position:absolute;left:0;top:0;width:100%;background:var(--teal)}
.letterhead .header-band{height:113px}
.business-card .header-band{height:71px}
.brand-mark{position:absolute;left:0;width:100%;display:flex;justify-content:center;align-items:center;gap:10px;font-family:"Jost",Futura,sans-serif;font-weight:500;color:var(--paper);letter-spacing:2px;white-space:nowrap}
.brand-mark .mark-square{width:22px;height:22px;background:var(--paper);flex:none}
.letterhead .brand-mark{top:40px;font-size:30px;padding-right:10px}
.business-card .brand-mark{top:20px;font-size:26px}
.business-card .brand-mark .mark-square{width:19px;height:19px}
.wordmark{position:absolute;left:0;width:100%;text-align:center;font-family:"Jost",Futura,sans-serif;font-weight:500;color:var(--ink);letter-spacing:1px;white-space:nowrap}
.letterhead .wordmark{top:163px;font-size:27px;padding-right:12px}
.business-card .wordmark{top:116px;font-size:25px}
.contact-list{position:absolute;list-style:none;font-size:13.5px}
.contact-list li{display:flex;align-items:center;gap:7px;height:25px}
.contact-list svg{width:11px;height:11px;flex:none}
.letterhead .contact-list{left:608px;top:13px;color:var(--paper)}
.letterhead .contact-list li{height:30px}
.letterhead .contact-list svg{fill:var(--paper)}
.business-card .contact-list{left:253px;top:187px;color:var(--ink)}
.business-card .contact-list svg{fill:var(--teal)}
.person{position:absolute;right:292px;top:186px;text-align:right;font-size:13.5px;line-height:20px}
.person-name{color:var(--teal);font-family:"Jost",Futura,sans-serif;font-size:15px;letter-spacing:.5px}
.divider{position:absolute;left:240px;top:190px;width:1px;height:74px;background:#b5b5b5}
.footer-address{position:absolute;left:0;bottom:12px;width:100%;text-align:center;font-size:13.5px}
</style>
</head>
<body>

<section class="letterhead">
  <div class="header-band">
    <div class="brand-mark"><span class="mark-square"></span>PELWICK</div>
    <ul class="contact-list">
      <li><svg viewBox="0 0 10 10"><path d="M2 0h2l1 3-1.5 1a6 6 0 0 0 2.5 2.5L7 5l3 1v2c0 1-1 2-2 2C4 10 0 6 0 2c0-1 1-2 2-2z"/></svg>123-456-7890</li>
      <li><svg viewBox="0 0 10 10"><path d="M0 2h10v6H0zM0 2l5 3 5-3v1L5 6 0 3z"/></svg>info@pelwickreno.com</li>
      <li><svg viewBox="0 0 10 10"><circle cx="5" cy="5" r="5"/></svg>www.pelwickreno.com</li>
    </ul>
  </div>
  <div class="wordmark">PELWICK RENOVATIONS</div>
  <p class="footer-address">00, complex name, street, city 00000</p>
</section>

<section class="business-card">
  <div class="header-band">
    <div class="brand-mark"><span class="mark-square"></span>PELWICK</div>
  </div>
  <div class="wordmark">PELWICK RENOVATIONS</div>
  <div class="person">
    <div class="person-name">YOUR NAME</div>
    <div>TITLE</div>
    <div>00, complex name</div>
    <div>street, city 00000</div>
  </div>
  <div class="divider"></div>
  <ul class="contact-list">
    <li><svg viewBox="0 0 10 10"><path d="M2 0h2l1 3-1.5 1a6 6 0 0 0 2.5 2.5L7 5l3 1v2c0 1-1 2-2 2C4 10 0 6 0 2c0-1 1-2 2-2z"/></svg>123-456-7890</li>
    <li><svg viewBox="0 0 10 10"><path d="M0 2h10v6H0zM0 2l5 3 5-3v1L5 6 0 3z"/></svg>info@pelwickreno.com</li>
    <li><svg viewBox="0 0 10 10"><circle cx="5" cy="5" r="5"/></svg>www.pelwickreno.com</li>
  </ul>
</section>

</body>
</html>
```